Simple elegant business card

General card for a fin and television director.
Just want name, email, phone and address.

Target Market(s)

Prospective employers

Industry/Entity Type

Business

Requirements
Must have
• As above
Nice to have
• Logo but not necessary.
Should not have
• Not too colourful or funky.
• Simplicity and elegance the way to go.

```html
<!DOCTYPE html>
<html lang="en">
<head>
<meta charset="utf-8">
<title>Nora Ellison — Film Director</title>
<link rel="stylesheet" href="https://fonts.googleapis.com/css2?family=Roboto+Slab:wght@200;300&display=swap">
<style>
  :root {
    --ink: #000000;
    --paper: #ffffff;
    --royal-blue: #2129cf;
    --type-light: #ffffff;
  }
  html, body {
    margin: 0;
    padding: 0;
    width: 1200px;
    height: 692px;
    overflow: hidden;
    background: var(--paper);
  }
  .business-card {
    position: relative;
    width: 1200px;
    height: 692px;
    box-sizing: border-box;
    border: 5px solid var(--ink);
    background: var(--paper);
    overflow: hidden;
    font-family: "Roboto Slab", Georgia, serif;
    color: var(--type-light);
  }
  .wave-panel {
    position: absolute;
    inset: 0;
    width: 100%;
    height: 100%;
    display: block;
  }
  .wave-panel path { fill: var(--royal-blue); }
  .contact-block {
    position: absolute;
    right: 42px;
    top: 100px;
    text-align: right;
    font-weight: 300;
    font-size: 32px;
    line-height: 47px;
    letter-spacing: 0.2px;
    white-space: nowrap;
  }
  .contact-block p { margin: 0; }
  .identity-block {
    position: absolute;
    right: 42px;
    top: 472px;
    text-align: right;
    white-space: nowrap;
  }
  .person-name {
    margin: 0;
    font-weight: 200;
    font-size: 84px;
    line-height: 96px;
    letter-spacing: 0.5px;
  }
  .person-role {
    margin: 6px 0 0;
    font-weight: 300;
    font-size: 25px;
    line-height: 32px;
  }
</style>
</head>
<body>
  <main class="business-card">
    <svg class="wave-panel" viewBox="0 0 1190 682" preserveAspectRatio="none" aria-hidden="true">
      <path d="M565 0 C592 70 598 130 588 190 C572 280 518 340 492 425 C465 515 472 610 537 682 L1190 682 L1190 0 Z"/>
    </svg>
    <section class="contact-block">
      <p class="contact-phone">Mobile: +(1) 310 555 0142</p>
      <p class="contact-email">e-mail: nora.ellison@example.com</p>
    </section>
    <section class="identity-block">
      <h1 class="person-name">Nora Ellison</h1>
      <p class="person-role">Film Director</p>
    </section>
  </main>
</body>
</html>
```